Tovlen Systems New Website - IT Infrastructure | Smart Cabinet | Micro Data Center

We're an IT SI providing Server Room Design & Build | All-in-One Rack & Smart Cabinet | Structured Cabling | IT Relocation | Maintenance. Old website can be found at www.tovlensys.com.hk. We'd like a brand new wix website which is modern, minimalist, interactive with some animation. Website content will be mostly static and include our service, our project, news and events, about us, contacts, blogs, partners and brands, etc.

reference sites:
We'd like to see more designs referring to below

https://www.pixelbazar.example/design/51730264
https://www.pixelbazar.example/design/51869047
https://vellhorn.example/

Animation (scrolling effect) referring to
https://vellhorn.example/intelligence/smart-office-room/
Updates

we'd like below style.

Designs look the same

Target Market(s)

Commercials in HK

Industry/Entity Type

IT, Technology, Data Center

Coding

Coded - Design and coding required

Font styles to use
Sans Serif

Requirements
Must have
• CMS, Some Interactive Elements/ Graphics

```html
<!DOCTYPE html>
<html lang="en">
<head>
<meta charset="utf-8">
<title>Tovlen Systems</title>
<link href="https://fonts.googleapis.com/css2?family=Poppins:ital,wght@0,300;0,400;0,500;1,300&display=swap" rel="stylesheet">
<style>
:root{
  --red:#d4381f;
  --black:#000;
  --white:#fff;
  --ink:#222;
  --muted:#555;
  --soft:#f7f7f7;
  --star:#f0a21b;
}
*{margin:0;padding:0;box-sizing:border-box}
html,body{width:1200px;height:4766px;overflow:hidden}
body{position:relative;font-family:'Poppins',sans-serif;color:var(--ink);background:var(--white)}
.abs{position:absolute}
.fill{border-radius:4px}
/* header */
.site-header{left:0;top:0;width:1200px;height:129px;background:var(--black)}
.brand{left:88px;top:38px;display:flex;align-items:center;gap:14px;color:var(--white);font-size:34px;font-weight:500}
.brand-mark{width:48px;height:48px;border:4px solid var(--white)}
.nav{left:468px;top:52px;display:flex;gap:22px;font-size:15px;color:var(--white)}
.nav .active{color:var(--red);border-bottom:2px solid var(--red);padding-bottom:4px}
.btn{display:inline-block;background:var(--red);color:var(--white);font-size:17px;text-align:center}
.nav-cta{left:996px;top:46px;width:120px;height:38px;line-height:38px;font-size:15px}
/* hero */
.hero-photo{left:85px;top:187px;width:431px;height:471px;background:linear-gradient(180deg,#2f3436 0%,#6d7173 45%,#c9cbcc 100%);border-radius:6px}
.hero-title{left:380px;top:262px;font-size:46px;font-weight:300;font-style:italic;line-height:62px;color:var(--red)}
.hero-title .lead{color:var(--white)}
.hero-title .second{padding-left:152px}
.hero-copy{left:530px;top:404px;width:520px;font-size:15px;line-height:21px;color:var(--muted)}
.watch{left:531px;top:508px;display:flex;align-items:center;gap:10px;font-size:18px;color:var(--muted)}
.play{width:44px;height:44px}
.hero-more{left:734px;top:504px;width:176px;height:52px;line-height:52px}
/* partners band */
.partners{left:0;top:717px;width:1200px;height:134px;background:var(--red)}
.partner{top:32px;height:68px;background:rgba(255,255,255,.92)}
.dots{display:flex;gap:8px;justify-content:center}
.dots span{width:9px;height:9px;border-radius:50%;background:var(--red)}
.partners .dots span{background:var(--white)}
/* section title */
.section-title{left:0;width:1200px;text-align:center;font-size:54px;font-weight:400;color:var(--red)}
/* services */
.service{width:506px;height:511px;background:var(--white);box-shadow:0 2px 8px rgba(0,0,0,.14);text-align:center}
.service .photo{height:287px;width:100%}
.service h3{margin-top:30px;font-size:20px;font-weight:400;color:var(--red);text-transform:uppercase}
.service p{margin:10px auto 0;width:460px;font-size:15px;line-height:22px;color:var(--muted)}
.service .btn{margin-top:22px;width:176px;height:42px;line-height:42px}
/* about */
.about{left:0;top:2154px;width:1200px;height:583px;background:var(--red);color:var(--white)}
.about h2{position:absolute;left:82px;top:95px;font-size:33px;font-weight:400}
.about .text{position:absolute;left:82px;top:155px;width:540px;font-size:15px;line-height:22px}
.about .text p{margin-bottom:22px}
.about ul{list-style:none;margin-top:-2px}
.about li{position:relative;padding-left:22px;margin-bottom:10px}
.about li::before{content:"";position:absolute;left:0;top:8px;width:8px;height:8px;border-radius:50%;background:var(--white)}
.about-photo{left:690px;top:54px;width:430px;height:471px;background:linear-gradient(90deg,#2b2a2c 0%,#8b3b22 45%,#d0652d 60%,#3a3b3e 100%);border-radius:8px}
/* projects */
.project{background:#ccc}
/* testimonials */
.testimonials{left:0;top:3741px;width:1200px;height:517px;background:var(--soft)}
.review{top:184px;width:333px;height:235px;background:var(--white);box-shadow:0 1px 6px rgba(0,0,0,.08);text-align:center}
.avatar{width:66px;height:66px;border-radius:50%;margin:18px auto 0;background:linear-gradient(180deg,#b7896a,#5b3b2c)}
.stars{margin-top:6px;color:var(--star);font-size:15px;letter-spacing:1px}
.review .name{font-size:17px;color:var(--ink);margin-top:2px}
.review .role{font-size:15px;color:var(--red);font-style:italic;font-weight:300}
.review p{width:290px;margin:8px auto 0;font-size:13px;line-height:19px;color:var(--muted)}
/* footer */
.footer{left:0;top:4258px;width:1200px;height:396px;background:var(--red);color:var(--white)}
.footer h4{position:absolute;top:90px;font-size:21px;font-weight:400}
.footer ul{position:absolute;top:172px;list-style:none;font-size:15px}
.footer li{height:31px}
.footer li::before{content:"›";margin-right:14px}
.contact-row{position:absolute;left:756px;display:flex;gap:20px;font-size:14px;line-height:19px}
.contact-icon{flex:none;width:30px;height:30px}
.bottom-bar{left:0;top:4654px;width:1200px;height:112px;background:var(--black);color:var(--white)}
.social{position:absolute;left:86px;top:36px;display:flex;gap:8px}
.social span{width:42px;height:42px;border:2px solid var(--white);border-radius:50%}
.copyright{position:absolute;right:90px;top:46px;font-size:15px}
</style>
</head>
<body>

<header class="site-header abs">
  <div class="brand abs"><span class="brand-mark"></span>Tovlen Systems</div>
  <nav class="nav abs">
    <span class="active">Home</span><span>About Us</span><span>Our Services</span><span>Our Projects</span><span>Testimonials</span>
  </nav>
  <span class="btn nav-cta abs">Contact Us</span>
</header>

<section>
  <div class="hero-photo abs" role="img" aria-label="Data center hall with raised floor and server racks"></div>
  <h1 class="hero-title abs"><span class="lead">Tovlen</span> Systems<br><span class="second">Solutions Limited</span></h1>
  <p class="hero-copy abs">Tovlen Systems is well experienced in delivering the best in Data Network Infrastructure, Structured Cabling, Telephony, Migration and Maintenance solutions.</p>
  <div class="watch abs">
    <svg class="play" viewBox="0 0 44 44"><circle cx="22" cy="22" r="22" fill="#d4381f"/><path d="M17 13 L31 22 L17 31Z" fill="#fff"/></svg>
    Watch Videos
  </div>
  <span class="btn hero-more abs">Read More</span>
</section>

<section class="partners abs" aria-label="Partners">
  <div class="partner abs" style="left:88px;width:160px;border-radius:4px"></div>
  <div class="partner abs" style="left:290px;width:182px;border-radius:40px"></div>
  <div class="partner abs" style="left:512px;width:190px;border-radius:4px"></div>
  <div class="partner abs" style="left:732px;width:168px;border-radius:4px"></div>
  <div class="partner abs" style="left:936px;width:174px;border-radius:34px"></div>
  <div class="dots abs" style="left:0;top:109px;width:1200px"><span></span><span></span><span></span></div>
</section>

<h2 class="section-title abs" style="top:895px">Our Services</h2>

<article class="service abs" style="left:89px;top:1011px">
  <div class="photo" role="img" aria-label="Patch panel with blue network cables" style="background:linear-gradient(180deg,#1e3a44,#3f8aa0 50%,#1b2a2e)"></div>
  <h3>Data Center Design and Build</h3>
  <p>Data Center is like a brain to a business deserving and demanding top-level attention and tremendous resources from time to time.</p>
  <span class="btn">Read More</span>
</article>
<article class="service abs" style="left:605px;top:1011px">
  <div class="photo" role="img" aria-label="Meeting room with long table and green accent wall" style="background:linear-gradient(90deg,#9cbf2f 0%,#e9e9e6 35%,#dcdcdc 70%,#3c4450 100%)"></div>
  <h3>Structured Cabling and Fiber Backbone</h3>
  <p>Data Center is like a brain to a business deserving and demanding top-level attention and tremendous resources from time to time.</p>
  <span class="btn">Read More</span>
</article>
<article class="service abs" style="left:89px;top:1548px">
  <div class="photo" role="img" aria-label="Office window overlooking city buildings" style="background:linear-gradient(180deg,#2b2d2f,#b6b8b5 50%,#6e706d)"></div>
  <h3>All-in-One Rack / Micro-Data Center</h3>
  <p>Data Center is like a brain to a business deserving and demanding top-level attention and tremendous resources from time to time.</p>
  <span class="btn">Read More</span>
</article>
<article class="service abs" style="left:605px;top:1548px">
  <div class="photo" role="img" aria-label="Ceiling with wireless access point and cable tray" style="background:linear-gradient(135deg,#d8d8d6,#b9bab8 60%,#8f908e)"></div>
  <h3>Audiovisual and Conference Room</h3>
  <p>Data Center is like a brain to a business deserving and demanding top-level attention and tremendous resources from time to time.</p>
  <span class="btn">Read More</span>
</article>

<section class="about abs">
  <h2>About Tovlen Systems</h2>
  <div class="text">
    <p>Tovlen Systems is well experienced in delivering the best in Data Center professionalism that they deserved.</p>
    <p>Business needs with unbiased recommendation, but we also help IT Professionals create the most cost-effective solution and best uptime that meets their ever-changing demand.</p>
    <ul>
      <li>Data Center / Server Room Design and Build</li>
      <li>Structured Cabling Solution</li>
      <li>Data and Voice Networks, IP-Telephony Solution</li>
      <li>WiFi Solution / Relocation and Migration Service</li>
      <li>AV and Conference Room System</li>
    </ul>
  </div>
  <div class="about-photo abs" role="img" aria-label="Glass meeting pod with orange curtains"></div>
</section>

<h2 class="section-title abs" style="top:2789px">Our Projects</h2>
<div class="project abs" role="img" aria-label="Fire extinguisher against metal wall" style="left:118px;top:2905px;width:302px;height:468px;background:linear-gradient(90deg,#8e9092,#b8322a 45%,#c9cacb)"></div>
<div class="project abs" role="img" aria-label="Pole with security cameras against pale sky" style="left:429px;top:2905px;width:651px;height:242px;background:linear-gradient(180deg,#e4e8ef,#d3d9e2)"></div>
<div class="project abs" role="img" aria-label="Technician working on electrical panel" style="left:429px;top:3158px;width:338px;height:215px;background:linear-gradient(135deg,#d9d9d6,#3b5e8a 55%,#e5d35a)"></div>
<div class="project abs" role="img" aria-label="Loose wires hanging from green wall box" style="left:778px;top:3158px;width:302px;height:466px;background:linear-gradient(90deg,#2f5b33 0%,#3c6e3f 40%,#dcdedb 60%,#eceeea)"></div>
<div class="project abs" role="img" aria-label="Two security cameras mounted on grey wall" style="left:118px;top:3382px;width:649px;height:238px;background:linear-gradient(180deg,#5d6164,#3d4043)"></div>
<div class="dots abs" style="left:0;top:3670px;width:1200px"><span></span><span></span><span></span></div>

<section class="testimonials abs">
  <h2 class="section-title abs" style="top:60px">What The Client Says</h2>
  <div class="review abs" style="left:89px">
    <div class="avatar" role="img" aria-label="Client portrait"></div>
    <div class="stars">★★★★★</div>
    <div class="name">Marla Quint</div><div class="role">Organiser</div>
    <p>Lorem ipsum dolor sit amet, consectetur dolore lacus vel facilisis.</p>
  </div>
  <div class="review abs" style="left:433px">
    <div class="avatar" role="img" aria-label="Client portrait"></div>
    <div class="stars">★★★★★</div>
    <div class="name">Marla Quint</div><div class="role">Organiser</div>
    <p>Lorem ipsum dolor sit amet, consectetur dolore lacus vel facilisis.</p>
  </div>
  <div class="review abs" style="left:777px">
    <div class="avatar" role="img" aria-label="Client portrait"></div>
    <div class="stars">★★★★★</div>
    <div class="name">Marla Quint</div><div class="role">Organiser</div>
    <p>Lorem ipsum dolor sit amet, consectetur dolore lacus vel facilisis.</p>
  </div>
  <div class="dots abs" style="left:0;top:467px;width:1200px"><span></span><span></span><span></span></div>
</section>

<footer class="footer abs">
  <h4 style="left:207px">Quick Links</h4>
  <ul style="left:212px"><li>Home</li><li>About Us</li><li>Our Services</li><li>Our Projects</li><li>Testimonials</li></ul>
  <h4 style="left:490px">Customer Services</h4>
  <ul style="left:494px"><li>Contact us</li><li>Site Map</li><li>Terms and Use</li><li>My Account</li></ul>
  <h4 style="left:756px">Contact Us</h4>
  <div class="contact-row" style="top:168px">
    <svg class="contact-icon" viewBox="0 0 30 30"><rect x="1" y="1" width="28" height="28" rx="6" fill="none" stroke="#fff" stroke-width="2"/><path d="M10 9c1 5 5 10 11 12l2-3-3-2-2 1c-2-1-4-3-5-5l1-2-2-3z" fill="#fff"/></svg>
    <div>CALL US<br>+852 3170 4410 / +852 6620 1938</div>
  </div>
  <div class="contact-row" style="top:226px">
    <svg class="contact-icon" viewBox="0 0 30 30"><rect x="1" y="1" width="28" height="28" rx="6" fill="none" stroke="#fff" stroke-width="2"/><rect x="8" y="10" width="14" height="10" fill="none" stroke="#fff" stroke-width="1.6"/><path d="M8 10l7 6 7-6" fill="none" stroke="#fff" stroke-width="1.6"/></svg>
    <div>EMAIL US<br>marketing@tovlensys.com.hk</div>
  </div>
  <div class="contact-row" style="top:282px">
    <svg class="contact-icon" viewBox="0 0 30 30"><rect x="1" y="1" width="28" height="28" rx="6" fill="none" stroke="#fff" stroke-width="2"/><path d="M15 7a6 6 0 0 1 6 6c0 5-6 11-6 11s-6-6-6-11a6 6 0 0 1 6-6z" fill="#fff"/><circle cx="15" cy="13" r="2.2" fill="#d4381f"/></svg>
    <div style="width:290px">Rm 905, 9/F, Harbourline Centre, 18 Kin Wah Road, Kwun Tong, Kowloon, Hong Kong</div>
  </div>
</footer>

<div class="bottom-bar abs">
  <div class="social" aria-label="Social links"><span></span><span></span><span></span><span></span></div>
  <div class="copyright">All Rights Reserved @ Copyrights 2023</div>
</div>

</body>
</html>
```